BRISKA sparkling water needs new artwork! Based in Southern California

"Briska" is a new sparkling water company based in Southern California that offers refreshing flavors (lime, cherry, & mango) with B vitamins and antioxidants.

We would like to see packaging designs for standard 12oz cans for each of the three flavors.
Our initial preference is to have individual artwork for each flavor.

Attached are examples of competitors' designs.
Updates

We are extending the deadline for the Thanksgiving Holiday. Thank you all for your contributions.

```html
<!DOCTYPE html>
<html lang="en">
<head>
<meta charset="utf-8">
<title>Briska Sparkling Mango – Can Label</title>
<link rel="stylesheet" href="https://fonts.googleapis.com/css2?family=Marcellus&family=Alegreya:wght@800&family=Luckiest+Guy&family=Montserrat:wght@700;800&display=swap">
<style>
  :root {
    --backdrop: #e8e9eb;
    --orange-deep: #ff6a00;
    --orange-mid: #ff8a1c;
    --orange-light: #ffa53a;
    --yellow: #fdd10b;
    --yellow-warm: #fcc20a;
    --green-dark: #0f3b35;
    --white: #ffffff;
  }
  * { margin: 0; padding: 0; box-sizing: border-box; }
  html, body {
    width: 1200px; height: 910px; overflow: hidden;
    background: var(--backdrop);
  }
  .canvas { position: relative; width: 1200px; height: 910px; }
  .brand-banner { position: absolute; left: 40px; top: 210px; width: 480px; height: 300px; }
  .can-label { position: absolute; left: 580px; top: 70px; width: 600px; height: 738px;
    box-shadow: 0 6px 18px rgba(0,0,0,.12); }
  .wordmark { font-family: "Marcellus", serif; fill: var(--white); }
  .flavor-type { font-family: "Alegreya", serif; font-weight: 800; fill: var(--green-dark); }
  .flavor-name { font-family: "Luckiest Guy", "Arial Black", sans-serif; font-weight: 900; fill: var(--white);
    stroke: var(--orange-deep); stroke-width: 8; paint-order: stroke; stroke-linejoin: round; }
  .badge-text { font-family: "Montserrat", sans-serif; font-weight: 800; fill: var(--white); }
  .badge-letter { font-family: "Montserrat", sans-serif; font-weight: 800; fill: var(--orange-deep); }
  .volume { font-family: "Montserrat", sans-serif; font-weight: 700; fill: var(--green-dark); }
</style>
</head>
<body>
<main class="canvas">

  <svg class="brand-banner" viewBox="0 0 480 300" aria-label="Briska name banner">
    <defs>
      <linearGradient id="bannerFill" x1="0" y1="0" x2="0" y2="1">
        <stop offset="0" stop-color="#ff6a00"/>
        <stop offset="1" stop-color="#ffa53a"/>
      </linearGradient>
    </defs>
    <path d="M0 0 H480 V185 C380 150 250 160 140 205 C80 230 30 245 0 250 Z" fill="url(#bannerFill)"/>
    <path d="M405 205 C430 210 455 220 480 232 V255 C455 232 430 215 405 205 Z" fill="var(--orange-deep)"/>
    <text class="wordmark" x="240" y="112" font-size="92" text-anchor="middle">Briska</text>
  </svg>

  <svg class="can-label" viewBox="0 0 636 782" aria-label="Briska Sparkling Mango can label">
    <defs>
      <linearGradient id="fruitFill" x1="0" y1="0" x2="0" y2="1">
        <stop offset="0" stop-color="#ffb030"/>
        <stop offset="0.6" stop-color="#ff9420"/>
        <stop offset="1" stop-color="#fcc20a"/>
      </linearGradient>
    </defs>
    <rect class="label-ground" width="636" height="782" fill="var(--yellow)"/>
    <path class="top-band" d="M0 0 H636 V150 C540 120 420 170 300 185 C190 200 80 185 0 200 Z" fill="var(--orange-deep)"/>
    <path class="top-band-light" d="M0 200 C80 185 190 200 300 185 C420 170 540 120 636 150 V170 C540 145 420 190 300 205 C190 218 80 210 0 225 Z" fill="var(--orange-mid)"/>
    <path class="accent-swoosh" d="M230 245 C320 265 420 262 520 232 C430 280 320 285 230 245 Z" fill="var(--orange-mid)"/>
    <text class="wordmark" x="48" y="90" font-size="46">Briska</text>

    <rect class="fruit-art" x="205" y="290" width="410" height="470" rx="60"
      fill="url(#fruitFill)" opacity=".8" role="img"
      aria-label="Illustration of a whole mango with a green leaf and a cubed mango half"/>

    <rect class="name-stripe" x="112" y="250" width="80" height="440" fill="var(--white)"/>
    <text class="flavor-type" transform="translate(172 672) rotate(-90)" font-size="60">Sparkling</text>

    <text class="flavor-name" x="222" y="520" font-size="84" textLength="380" lengthAdjust="spacingAndGlyphs">MANGO</text>

    <g class="vitamin-badge">
      <path d="M206 700 C206 670 240 660 270 662 C310 664 340 690 330 730 L310 770 H206 Z" fill="var(--orange-deep)"/>
      <circle cx="268" cy="700" r="17" fill="var(--white)"/>
      <text class="badge-letter" x="268" y="708" font-size="22" text-anchor="middle">B</text>
      <text class="badge-text" x="268" y="736" font-size="19" text-anchor="middle">vitamins</text>
      <text class="badge-text" x="268" y="750" font-size="10" text-anchor="middle">&amp; antioxidants</text>
    </g>

    <text class="volume" x="370" y="738" font-size="13">Cont</text>
    <text class="volume" x="370" y="751" font-size="13">Net.</text>
    <text class="volume" x="408" y="752" font-size="26" font-style="italic">12</text>
    <text class="volume" x="445" y="752" font-size="22">fl.oz</text>
  </svg>

</main>
</body>
</html>
```